Bright Quest Appeal needs a brochure

I need an A4 - Two sided brochure design.
It's for a maths challenge fundraiser for primary schools throughout Australia.
It needs to be bright and fun with the pictures / files supplied,
Please use as many pics as you can, more the better...
Also keep Logos as transparent
See our website for an idea of what we do pls. thebrightquest.example
Pls make it FUN ....NOT corporate..
so curves and colours rather than straight lines
The only headings that need to be ALL capitals is "FREE TO JOIN" & "FUNDRAISER" Other titles not all capitals pls
Please note: when putting in the pics of the games, pls put in order from game1-7 as they go in order of the school grade levels (Preschool to Grade 6). showing teachers how they become more difficult...in that order.
This brochure will be sent to schools.
Schools have admin open letters, we get about 2 - 3 seconds for admin to decide to keep or bin the brochure, so they need to see it's a fundraiser and "free to join" in those seconds.
cheers
- fun style maybe marker felt or comic sans but you choose any other you think works to make it fun

```html
<!DOCTYPE html>
<html lang="en">
<head>
<meta charset="utf-8">
<title>Bright Quest Appeal – Maths Challenge Flyer</title>
<link href="https://fonts.googleapis.com/css2?family=Kalam:wght@700&family=PT+Sans:wght@400&family=PT+Sans+Narrow:wght@700&display=swap" rel="stylesheet">
<style>
  :root {
    --red: #e10a23;
    --teal: #a8dadb;
    --white: #ffffff;
    --ink: #111111;
    --gold: #c9a23a;
    --script: "Kalam", cursive;
    --body: "PT Sans", sans-serif;
    --narrow: "PT Sans Narrow", sans-serif;
  }
  * { margin: 0; padding: 0; box-sizing: border-box; }
  html, body { width: 848px; height: 1200px; overflow: hidden; background: var(--white); }
  .flyer {
    position: relative; width: 848px; height: 1200px; overflow: hidden;
    background: var(--white); border: 1px solid var(--ink);
  }
  .hero-photo {
    position: absolute; left: 0; top: 0; width: 848px; height: 390px;
    background: linear-gradient(180deg, #c9a88f 0%, #d8c3b3 35%, #e7dfd8 65%, #ffffff 100%);
  }
  .shadowed { position: absolute; }
  .shadowed::before {
    content: ""; position: absolute; left: 11px; top: 11px; right: -11px; bottom: -11px;
    background: var(--teal); border-radius: inherit; z-index: 0;
  }
  .shadowed > * { position: relative; z-index: 1; }
  .info-panel {
    left: 80px; top: 148px; width: 677px; height: 486px;
    border-radius: 32px 0 54px 0;
  }
  .info-panel .panel-fill {
    position: absolute; inset: 0; background: var(--red); border-radius: 32px 0 54px 0;
  }
  .headline {
    font-family: var(--script); color: var(--white); text-align: center;
    font-size: 43px; line-height: 1; position: absolute; left: 0; right: 0; top: 16px;
  }
  .subhead {
    font-family: var(--script); color: var(--white); text-align: center;
    font-size: 28px; line-height: 1; position: absolute; left: 0; right: 0; top: 70px;
  }
  .easy-bar {
    position: absolute; left: 23px; top: 115px; width: 631px; height: 69px;
    background: var(--white); border-radius: 30px 0 30px 0;
    font-family: var(--script); color: var(--red); font-size: 44px;
    text-align: center; line-height: 76px;
  }
  .how-title {
    font-family: var(--script); color: var(--white); text-align: center;
    font-size: 42px; line-height: 1; position: absolute; left: 0; right: 0; top: 196px;
  }
  .steps {
    position: absolute; left: 22px; right: 20px; top: 252px;
    list-style: none; font-family: var(--body); color: var(--white);
    font-size: 18.5px; line-height: 24px;
  }
  .steps li { position: relative; padding-left: 18px; margin-bottom: 11px; }
  .steps li::before { content: "•"; position: absolute; left: 0; font-size: 14px; }
  .games-title {
    position: absolute; left: 0; right: 0; top: 664px; text-align: center;
    font-family: var(--script); color: var(--red); font-size: 30px; line-height: 1;
  }
  .game-tile { width: 142px; height: 94px; border-radius: 10px 0 14px 0; }
  .game-tile .shot { width: 142px; height: 94px; border-radius: 10px 0 14px 0; }
  .shot-space { background: linear-gradient(135deg, #3a2a6e, #7a3c8a); }
  .shot-money { background: linear-gradient(135deg, #5c7fc9, #8a6b4e); }
  .shot-chance { background: linear-gradient(135deg, #34b03c, #7fd04a); }
  .shot-clocks { background: linear-gradient(135deg, #1e4fa0, #e0c23a); }
  .shot-area { background: linear-gradient(135deg, #f1ede4, #2f5fbf); }
  .shot-angles { background: linear-gradient(135deg, #0c1a33, #2a3f66); }
  .shot-decimals { background: linear-gradient(135deg, #2a2a2a, #5a5a4a); }
  .cta-box { left: 81px; top: 966px; width: 498px; height: 184px; border-radius: 30px 0 50px 0; }
  .cta-box .panel-fill { position: absolute; inset: 0; background: var(--red); border-radius: 30px 0 50px 0; }
  .cta-text { position: absolute; left: 0; right: 0; text-align: center; color: var(--white); font-family: var(--narrow); font-weight: 700; line-height: 1; }
  .cta-lead { top: 29px; font-size: 25px; }
  .cta-url { top: 63px; font-size: 33px; }
  .cta-call { top: 111px; font-size: 56px; letter-spacing: -0.5px; }
  .promoter { position: absolute; left: 590px; top: 962px; width: 208px; text-align: center; }
  .promoter-mark { width: 100px; height: 100px; border-radius: 50%; background: var(--ink); margin: 4px auto 0; }
  .promoter-name { margin-top: 8px; font-family: var(--narrow); font-weight: 700; font-size: 16px; line-height: 17px; color: var(--ink); letter-spacing: 0.5px; }
  .promoter-by { margin-top: 6px; font-family: var(--narrow); font-weight: 700; font-size: 15px; color: var(--ink); line-height: 20px; }
</style>
</head>
<body>
<main class="flyer">
  <div class="hero-photo" role="img" aria-label="Photo of five cheerful young students hugging in a classroom"></div>

  <section class="shadowed info-panel">
    <div class="panel-fill"></div>
    <h1 class="headline">All set up online for you!</h1>
    <p class="subhead">Builds confidence in maths for students!</p>
    <div class="easy-bar">Easy to run!</div>
    <h2 class="how-title">Here is how it works:</h2>
    <ul class="steps">
      <li>Let us know how many memberships you need for your Bright Quest Appeal.</li>
      <li>We will send you our website access code for those memberships.</li>
      <li>Download our fundraising letter, photocopy and give to parents to collect funds. (See our website for more details.)</li>
      <li>On the website, each year level has a set of maths challenges for students to solve.</li>
      <li>Once completed students may download a certificate of congratulations.</li>
    </ul>
  </section>

  <h2 class="games-title">Over 260 maths games for Foundation to Grade 6!</h2>

  <div class="shadowed game-tile" style="left:87px;top:720px"><div class="shot shot-space" role="img" aria-label="Game 1: shapes and objects matching in space"></div></div>
  <div class="shadowed game-tile" style="left:264px;top:720px"><div class="shot shot-money" role="img" aria-label="Game 2: ice cream prices and coins"></div></div>
  <div class="shadowed game-tile" style="left:442px;top:720px"><div class="shot shot-chance" role="img" aria-label="Game 3: chance and likelihood with coloured balls"></div></div>
  <div class="shadowed game-tile" style="left:620px;top:720px"><div class="shot shot-clocks" role="img" aria-label="Game 4: telling the time with clocks"></div></div>
  <div class="shadowed game-tile" style="left:87px;top:835px"><div class="shot shot-area" role="img" aria-label="Game 5: area of bedrooms on a grid"></div></div>
  <div class="shadowed game-tile" style="left:264px;top:835px"><div class="shot shot-angles" role="img" aria-label="Game 6: measuring angles in space"></div></div>
  <div class="shadowed game-tile" style="left:442px;top:835px"><div class="shot shot-decimals" role="img" aria-label="Game 7: ordering decimals on stone tiles"></div></div>

  <section class="shadowed cta-box">
    <div class="panel-fill"></div>
    <p class="cta-text cta-lead">START A MATHS CHALLENGE FOR YOUR SCHOOL:</p>
    <p class="cta-text cta-url">www.thebrightquest.example</p>
    <p class="cta-text cta-call">OR CALL 1300 555 010</p>
  </section>

  <aside class="promoter">
    <div class="promoter-mark"></div>
    <p class="promoter-name">RAISE4 CLASSROOMS</p>
    <p class="promoter-by">PROMOTED BY:<br>www.raise4classrooms.example</p>
  </aside>
</main>
</body>
</html>
```